Home Page Design for Birch Ridge Gear

We need a homepage design for Birch Ridge Gear, a company that sells ice fishing and cold weather products.

Current Website: https://www.birchridgegear.com/

Logo Design and Product images: https://files.example-share.net/folders/7QmXvT2pLk9RwZ4nB8cYdHs3JfGaUeN0?usp=sharing

*There is info on imagery in the homepage template. Where there isn't, appropriate stock imagery is acceptable.

Number of Pages Required

1 page

```html
<!DOCTYPE html>
<html lang="en">
<head>
<meta charset="utf-8">
<title>Birch Ridge Gear – Ice Fishing Gear</title>
<link href="https://fonts.googleapis.com/css2?family=Oswald:wght@500;700&family=Kaushan+Script&family=Poppins:wght@400;500;600&display=swap" rel="stylesheet">
<style>
:root{
  --red:#e3201b;
  --ink:#141414;
  --muted:#555;
  --white:#fff;
  --line:#d6d6d6;
  --sky:#a9c3dc;
  --ice:#e9eef3;
  --water-deep:#1e7fc4;
  --water-light:#bfe3f7;
}
*{margin:0;padding:0;box-sizing:border-box}
html,body{width:1200px;height:5188px;overflow:hidden;background:var(--white)}
body{font-family:"Poppins",sans-serif;color:var(--ink);position:relative}
.abs{position:absolute}
.h-title{font-family:"Oswald",sans-serif;font-weight:700;text-transform:uppercase;color:var(--ink)}
.script{font-family:"Kaushan Script",cursive;color:var(--red)}
.btn{display:inline-block;font-family:"Poppins",sans-serif;font-weight:600;font-size:13px;text-transform:uppercase;padding:10px 18px;color:var(--white);background:var(--red);text-decoration:none}
.btn.outline{background:transparent;border:2px solid var(--white)}
.photo{border-radius:6px}

/* header */
.site-header{top:0;left:0;width:1200px;height:58px;background:var(--white);border-top:5px solid var(--red);z-index:3}
.brand{left:160px;top:6px;font-family:"Oswald",sans-serif;font-weight:700;font-size:26px;color:var(--red);line-height:1;text-transform:uppercase;width:140px}
.nav{right:120px;top:14px;display:flex;align-items:center;gap:36px;font-size:12px;font-weight:500;text-transform:uppercase}
.nav a{color:var(--ink);text-decoration:none}

/* hero */
.hero{top:0;left:0;width:1200px;height:648px;background:linear-gradient(180deg,#7f99b4 0%,#a6bdd3 35%,#dfe7ee 62%,#c9d4de 100%)}
.hero-copy{left:160px;top:212px;width:560px}
.hero-copy .script{font-size:22px;margin-bottom:6px}
.hero-copy h1{font-family:"Oswald",sans-serif;font-weight:700;font-size:46px;line-height:1.1;color:var(--white);text-transform:uppercase}
.hero-copy h1 span{color:var(--red)}
.hero-actions{margin-top:24px;display:flex;gap:16px}

/* partners */
.section-title{left:0;width:1200px;text-align:center;font-size:34px}
.partners{top:820px;left:170px;width:860px;display:flex;justify-content:space-between}
.partner-badge{width:100px;height:100px;border-radius:50%;background:#e6e6e6;border:2px solid #cfcfcf}

.water{left:0;width:1200px;background:linear-gradient(180deg,rgba(255,255,255,0) 0%,var(--water-light) 30%,var(--water-deep) 60%,var(--water-light) 85%,rgba(255,255,255,0) 100%)}

/* video */
.video-title{top:1170px;z-index:2}
.video{left:240px;top:1244px;width:720px;height:356px;background:linear-gradient(180deg,#c7d3dd 0%,#eef2f5 55%,#dfe5ea 100%)}
.play{left:580px;top:1402px}

/* steps */
.subtitle{left:0;width:1200px;text-align:center;font-size:20px}
.step-photo{width:424px;height:280px;box-shadow:14px 14px 0 -4px var(--line)}
.step-photo.left{box-shadow:-10px -10px 0 0 var(--red)}
.step-copy{width:440px}
.step-copy .script{font-size:20px}
.step-copy h3{font-family:"Oswald",sans-serif;font-weight:700;font-size:30px;text-transform:uppercase;margin:2px 0 10px}
.step-copy p{font-size:12.5px;line-height:1.6;color:var(--muted)}

/* who */
.who-title{left:160px;top:3268px;font-size:34px}
.who-sub{left:160px;top:3318px;font-size:20px}
.who-text{left:632px;top:3260px;width:448px;font-size:14px;line-height:1.65;color:var(--muted)}
.who-photo{left:312px;top:3420px;width:576px;height:340px;background:linear-gradient(180deg,#b9c9d7 0%,#e8edf1 55%,#f6f8fa 100%)}

/* form */
.cta-title{top:4054px;font-size:30px}
.cta-sub{top:4104px;left:200px;width:800px;text-align:left;font-size:20px;line-height:1.4}
.field{border:1px solid #c9c9c9;border-radius:4px;height:34px;font-size:12px;color:#777;padding:9px 12px;background:var(--white)}
.submit{left:525px;top:4372px}

/* footer */
.footer-brand{left:160px;top:4730px;font-family:"Oswald",sans-serif;font-weight:700;font-size:40px;color:var(--red);text-transform:uppercase;line-height:1.05;width:240px}
.f-col{width:180px;font-size:12.5px;line-height:1.65}
.f-col h4{font-family:"Poppins",sans-serif;font-size:12px;font-weight:600;color:var(--red);text-transform:uppercase;margin-bottom:4px}
.f-col a{display:block;color:var(--ink);text-decoration:none}
.f-rule{left:160px;top:4940px;width:880px;height:1px;background:var(--line)}
.copyright{left:160px;top:4956px;font-size:12px}
.copyright span{color:var(--red)}
.socials{left:916px;top:4952px;display:flex;gap:8px}
.socials i{width:22px;height:22px;border-radius:50%;background:var(--ink);display:block}
</style>
</head>
<body>

<header class="site-header abs">
  <div class="brand abs">Birch Ridge Gear</div>
  <nav class="nav abs">
    <a href="#">Features</a><a href="#">About Us</a><a href="#">Contact Us</a><a href="#">Login</a>
    <a class="btn" href="#">Register for a demo</a>
  </nav>
</header>

<section class="hero abs" role="img" aria-label="Ice auger drilling into a frozen lake with snow and a treeline under a winter sky"></section>
<div class="hero-copy abs">
  <p class="script">Upgrade your ice fishing game this season</p>
  <h1>Elevate your ice fishing and <span>outdoor adventures</span> with premium gear.</h1>
  <div class="hero-actions">
    <a class="btn" href="#">Purchase a product</a>
    <a class="btn outline" href="#">Watch demo video</a>
  </div>
</div>

<h2 class="section-title h-title abs" style="top:720px">Our Trust Partner</h2>
<div class="partners abs">
  <span class="partner-badge"></span><span class="partner-badge"></span><span class="partner-badge"></span>
  <span class="partner-badge"></span><span class="partner-badge"></span><span class="partner-badge"></span>
</div>

<div class="water abs" style="top:990px;height:150px" role="img" aria-label="Splashing water band"></div>

<h2 class="section-title video-title h-title abs">Watch Our Videos</h2>
<div class="video photo abs" role="img" aria-label="Video still of an angler sitting by an ice hole on a frozen lake"></div>
<svg class="play abs" width="40" height="40" viewBox="0 0 40 40"><circle cx="20" cy="20" r="20" fill="#e3201b"/><path d="M16 12l12 8-12 8z" fill="#fff"/></svg>

<div class="water abs" style="top:1670px;height:160px" role="img" aria-label="Splashing water band"></div>

<h2 class="section-title h-title abs" style="top:1904px">How It Works</h2>
<p class="subtitle script abs" style="top:1962px">Effortless Protection: Snap-on Blade Protectors for Easy Installation and Reliable Auger Shielding</p>

<div class="step-photo left photo abs" style="left:168px;top:2060px;background:linear-gradient(180deg,#9fb6cc,#e7ecf0)" role="img" aria-label="Two anglers using an ice auger on a frozen lake"></div>
<div class="step-copy abs" style="left:632px;top:2120px">
  <p class="script">Step 01</p>
  <h3>Augers:</h3>
  <p>Safeguard your auger with Birch Ridge Gear custom-made blade protectors. Designed for ice fishing enthusiasts, our high-quality covers ensure secure and hassle-free installation, protecting your blades during transport and storage. Invest in ultimate auger protection for peace of mind on your fishing adventures.</p>
</div>

<div class="step-copy abs" style="left:160px;top:2400px">
  <p class="script">Step 02</p>
  <h3>Ice Rods:</h3>
  <p>Elevate your ice fishing experience with Birch Ridge Gear custom rods. Meticulously crafted for ultimate performance, our rods offer unmatched quality at factory prices. Featuring an award-winning full-grip hand tied action power, a precision ground fiberglass blank, neat stainless steel guides and a premium spinning reel seat, these rods deliver clean sensitivity and comfort. Designed by seasoned anglers, they blend form and function.</p>
</div>
<div class="step-photo photo abs" style="left:608px;top:2360px;background:linear-gradient(180deg,#8fa9c1,#dfe6ec)" role="img" aria-label="Angler holding an ice rod over a hole in the ice"></div>

<div class="step-photo left photo abs" style="left:168px;top:2760px;background:linear-gradient(180deg,#7a8a6f,#c9b79c)" role="img" aria-label="Hands holding a freshly caught fish with a hook remover"></div>
<div class="step-copy abs" style="left:632px;top:2780px">
  <p class="script">Step 03</p>
  <h3>Hook Removers:</h3>
  <p>Effortlessly remove hooks, preserve gear and fish with Birch Ridge Gear hook removers. Save time and money on the ice with our innovative tool. Its patented design ensures simple, safe and efficient removal of exposed jigs without damaging lines. Made in solid aluminum, our hook remover combines durability with a clean, rugged style.</p>
</div>

<div class="water abs" style="top:3070px;height:140px" role="img" aria-label="Splashing water band"></div>

<h2 class="who-title h-title abs">Who It's For</h2>
<p class="who-sub script abs">Gear Crafted for Ice Fishing Enthusiasts</p>
<p class="who-text abs">Birch Ridge Gear is dedicated to serving passionate ice fishing enthusiasts who crave premium gear designed to elevate their fishing experience. Our products are tailored to meet the needs of avid anglers who seek durability, functionality, and innovative solutions for their ice fishing adventures.</p>
<div class="who-photo photo abs" role="img" aria-label="Angler seated on a bucket fishing on a snowy lake with pine forest behind"></div>

<div class="water abs" style="top:3810px;height:190px" role="img" aria-label="Splashing water band"></div>

<h2 class="section-title cta-title h-title abs">Elevate Your Ice Fishing Experience Today!</h2>
<p class="cta-sub script abs">Shop Now for Premium Gear that Delivers Durability, Functionality, and Innovation. Start Fishing Like a Pro with Birch Ridge Gear</p>
<form>
  <div class="field abs" style="left:200px;top:4196px;width:256px">Full Name</div>
  <div class="field abs" style="left:472px;top:4196px;width:256px">Email Address</div>
  <div class="field abs" style="left:744px;top:4196px;width:256px">Phone Number</div>
  <div class="field abs" style="left:200px;top:4248px;width:800px;height:92px">Message</div>
  <a class="btn submit abs" href="#">Submit a demo</a>
</form>

<div class="water abs" style="top:4430px;height:140px" role="img" aria-label="Splashing water band"></div>

<footer>
  <div class="footer-brand abs">Birch Ridge Gear</div>
  <div class="f-col abs" style="left:464px;top:4640px"><h4>Quick Links</h4><a href="#">Home</a><a href="#">Features</a><a href="#">Media</a><a href="#">Shop</a><a href="#">Contact</a></div>
  <div class="f-col abs" style="left:660px;top:4640px"><h4>Legal</h4><a href="#">Privacy Policy</a><a href="#">Terms &amp; Conditions</a><a href="#">Sitemap</a><a href="#">FAQ</a></div>
  <div class="f-col abs" style="left:872px;top:4640px"><h4>Company</h4><a href="#">About Us</a><a href="#">Jobs</a><a href="#">Press</a><a href="#">Terms &amp; Policies</a></div>
  <div class="f-col abs" style="left:464px;top:4808px"><h4>Resources</h4><a href="#">Podcasts</a><a href="#">Resources Library</a><a href="#">Marketing Strategy</a><a href="#">Blog</a></div>
  <div class="f-col abs" style="left:660px;top:4808px"><h4>Features</h4><a href="#">Headline Analyzer</a><a href="#">Social Message</a><a href="#">Email Subject</a><a href="#">Customer Success</a></div>
  <div class="f-col abs" style="left:872px;top:4808px"><h4>How It Works</h4><a href="#">Augers</a><a href="#">Ice Rods</a><a href="#">Hook Removers</a></div>
  <div class="f-rule abs"></div>
  <p class="copyright abs">© copyright 2023 | <span>Birch Ridge Gear</span> | All rights reserved.</p>
  <div class="socials abs"><i></i><i></i><i></i><i></i><i></i></div>
</footer>

<div class="water abs" style="top:5010px;height:178px" role="img" aria-label="Splashing water band"></div>

</body>
</html>
```